依頼詳細
メインビジュアルのイメージはお祭りで酢だこをかついでいるようなイメージです。イラストor写真可。ただ、上半身裸は芳しくなく、ハッピ等を着ている方が望ましいです。
一番下商品名・価格・注文数・「注文コード」の枠を設けてください。

納期が早く(納品6/17の週)、一度修正あり(6/14頃)。そのため、スムーズな作業・連絡を取れる方ご提案お待ちしております。

ご不明点あればお気軽にご質問お待ちしております。
記載項目
添付チラシ参照ください。
サイズ
A4
ページ数
片面
希望イメージ
シンプル 複雑
単色 カラフル
暗い 明るい
日常 高級
遊び心 厳粛
未来的 伝統的
女性的 男性的
希望する色
赤系、青系、緑系、黄・オレンジ系
納品ファイル
• イラストレーター形式 (.ai)
補足説明
必ずお入れするものではありませんが、酢だこの写真追加しておきます。必要であればお使いください。

イラストイメージがクライアントに合致しました。この度はありがとうございました。

質の高い多くのご提案いただきまして、ありがとうございました。
今後も案件ありますので、ぜひご参加お待ちしております。

```html
<!DOCTYPE html>
<html lang="ja">
<head>
<meta charset="utf-8">
<title>酢だこ祭り 2019年8月</title>
<link rel="stylesheet" href="https://fonts.googleapis.com/css2?family=Dela+Gothic+One&family=Noto+Sans+JP:wght@400;700;900&family=Noto+Serif+JP:wght@500;700&display=swap">
<style>
:root{
  --red:#e3101b;
  --deep-red:#b4000c;
  --yellow:#fcd419;
  --orange:#f59a12;
  --ink:#1a1a1a;
  --white:#ffffff;
  --cream:#fff6d6;
}
*{margin:0;padding:0;box-sizing:border-box}
html,body{width:849px;height:1200px;overflow:hidden;background:#fff}
.flyer{position:relative;width:849px;height:1200px;overflow:hidden;
  background:radial-gradient(circle at 50% 42%,#fff1a6 0,var(--yellow) 30%,var(--orange) 85%);
  font-family:"Noto Sans JP",sans-serif;color:var(--ink)}
.curtain{position:absolute;left:0;top:0;width:849px;height:44px;
  background:repeating-linear-gradient(90deg,var(--red) 0 70px,var(--white) 70px 140px);
  border-bottom:4px solid var(--deep-red)}
.issue{position:absolute;left:290px;top:48px;width:270px;height:56px;background:var(--ink);
  color:var(--white);font:900 40px/56px "Noto Sans JP",sans-serif;text-align:center;letter-spacing:2px}
.title{position:absolute;left:50px;top:90px;font-family:"Dela Gothic One",sans-serif;
  font-size:196px;line-height:1;color:var(--red);-webkit-text-stroke:8px var(--white);
  paint-order:stroke fill;letter-spacing:-6px}
.title-side{position:absolute;left:660px;top:110px;writing-mode:vertical-rl;
  font-family:"Dela Gothic One",sans-serif;font-size:112px;line-height:1;color:var(--red);
  -webkit-text-stroke:7px var(--white);paint-order:stroke fill}
.scene{position:absolute;left:30px;top:300px;width:789px;height:360px;border-radius:40px;
  background:linear-gradient(180deg,rgba(230,80,60,.55),rgba(255,255,255,.35))}
.schedule{position:absolute;left:490px;top:440px;width:226px;height:150px;background:var(--red);
  border:4px solid var(--white);border-radius:14px;color:var(--white);text-align:center;padding-top:8px;
  white-space:nowrap}
.schedule .label{font:700 18px/1.3 "Noto Sans JP",sans-serif;color:var(--yellow)}
.schedule .date{font:900 28px/1.2 "Noto Sans JP",sans-serif;letter-spacing:-0.5px}
.schedule .date small{font-size:16px}
.schedule .delivery{display:flex;justify-content:center;align-items:center;gap:6px}
.schedule .note{font:700 12px/1.15 "Noto Sans JP",sans-serif;text-align:left}
.product-photo{position:absolute;left:92px;top:655px;width:190px;height:160px;border-radius:12px;
  background:linear-gradient(180deg,#f4f4f4,#d8a0a6);border:3px solid var(--white)}
.offer{position:absolute;top:690px;text-align:left}
.offer-one{left:296px}.offer-two{left:560px}
.offer .name{font:700 21px/1.3 "Noto Sans JP",sans-serif;display:flex;align-items:center;gap:5px}
.offer .num{display:inline-block;width:26px;height:26px;border-radius:50%;background:var(--red);
  color:var(--white);font-size:17px;line-height:26px;text-align:center}
.offer .price{font:900 62px/1.1 "Noto Sans JP",sans-serif;color:var(--red);
  -webkit-text-stroke:5px var(--white);paint-order:stroke fill;letter-spacing:-2px;margin-top:4px}
.offer .price .tax{font-size:20px;-webkit-text-stroke:3px var(--white);margin-right:4px;letter-spacing:0}
.offer .price .yen{font-size:34px}
.order{position:absolute;left:0;top:895px;width:849px;height:305px;background:var(--white);padding:14px 28px 0}
.order-head{display:flex;gap:20px}
.order-info{width:380px}
.order-title{background:var(--red);color:var(--white);font:700 26px/42px "Noto Sans JP",sans-serif;padding-left:14px}
.order-title small{font-size:18px;margin-left:10px}
.order-dates{font:700 16px/1.5 "Noto Sans JP",sans-serif;color:var(--red);margin-top:6px}
.order-dates span{color:var(--ink)}
.customer{flex:1;border:2px solid var(--ink)}
.customer div{height:40px;border-bottom:1px solid var(--ink);font:500 16px/40px "Noto Serif JP",serif;padding-left:10px}
.customer div:last-child{border-bottom:none}
.order-table{width:100%;margin-top:14px;border-collapse:collapse;font-family:"Noto Serif JP",serif}
.order-table th,.order-table td{border:2px solid var(--ink);height:38px;font-size:19px;font-weight:700;text-align:center}
.order-table th{background:var(--cream);font-size:16px}
.order-table td.item{text-align:left;padding-left:16px}
.order-table td.item small{font-size:15px}
.order-table td.price small,.order-table td.qty{font-size:13px}
.order-table td.qty{text-align:right;padding-right:10px}
.fineprint{font:400 11px/1.4 "Noto Sans JP",sans-serif;margin-top:6px}
</style>
</head>
<body>
<main class="flyer">
  <div class="curtain"></div>
  <div class="issue">2019年8月</div>
  <div class="scene" role="img" aria-label="法被姿の二人が大きな酢だこを担ぐ祭りのイラスト"></div>
  <h1 class="title">酢だこ</h1>
  <div class="title-side">祭り</div>

  <section class="schedule">
    <p class="label">ご注文締切日</p>
    <p class="date">7/19<small>(金)</small>・20<small>(土)</small></p>
    <p class="label">お届け予定日</p>
    <div class="delivery">
      <p class="date">8/7<small>(水)</small></p>
      <p class="note">から<br>順次配送</p>
    </div>
  </section>

  <div class="product-photo" role="img" aria-label="カップ入り酢だこの商品写真"></div>
  <div class="offer offer-one">
    <p class="name"><span class="num">1</span>酢だこ(無頭) 400g</p>
    <p class="price"><span class="tax">税込</span>3,380<span class="yen">円</span></p>
  </div>
  <div class="offer offer-two">
    <p class="name"><span class="num">2</span>酢だこ(無頭) 800g</p>
    <p class="price"><span class="tax">税込</span>5,780<span class="yen">円</span></p>
  </div>

  <section class="order">
    <div class="order-head">
      <div class="order-info">
        <h2 class="order-title">ご注文書<small>2019年8月 酢だこ祭り</small></h2>
        <p class="order-dates">ご注文締切日 <span>7/19(金)・20(土)まで</span><br>お届け予定日 <span>8/7(水)から順次配送</span></p>
      </div>
      <div class="customer">
        <div>お名前</div>
        <div>お電話</div>
      </div>
    </div>
    <table class="order-table">
      <tr><th style="width:46px"></th><th>商品名 / 規格</th><th style="width:150px">価格</th><th style="width:120px">注文数</th><th style="width:150px">注文コード</th></tr>
      <tr><td>1.</td><td class="item">酢だこ(無頭) <small>/ 400g</small></td><td class="price">3,380円<small>(税込)</small></td><td class="qty">個</td><td></td></tr>
      <tr><td>2.</td><td class="item">酢だこ(無頭) <small>/ 800g</small></td><td class="price">5,780円<small>(税込)</small></td><td class="qty">個</td><td></td></tr>
    </table>
    <p class="fineprint">※ ご記入いただいた情報は、商品の発送・ご連絡以外には使用いたしません。</p>
  </section>
</main>
</body>
</html>
```